Business Card and Stationary for an Executive and Life Coaching company
Harbor Kindle
Simple
Lina Brook, KLV, DRT
Executive Life Coach
2873 Wexbury Ln. Suite 615
Naples, FL 34782
Lina@HarborKindle.example
www.HarborKindle.example
I've included logo for KLV, and instructions on where and how to place it.
I'd like the design to be simple and uncluttered, while enticing people to want to be part of the movement and program because it is fun, smart, and provides tangible and positive results.
I'd like simple but unique fonts.
rise with purpose (on top)
(1 letter logo may go in the middle)
Guiding Driven Leaders and Founders Forward. (bottom of card)

```html
<!DOCTYPE html>
<html lang="en">
<head>
<meta charset="utf-8">
<title>Harbor Kindle Stationery</title>
<link href="https://fonts.googleapis.com/css2?family=Raleway:wght@400;600;700&display=swap" rel="stylesheet">
<style>
  :root {
    --bg: #e4e4e4;
    --paper: #ffffff;
    --green: #5f7a4f;
    --green-dark: #4a6140;
    --gold: #b8975a;
    --gold-light: #d6bd86;
    --gold-dark: #8f7140;
    --ink: #4b4b4b;
    --grey: #8a8a8a;
  }
  * { margin: 0; padding: 0; box-sizing: border-box; }
  html, body { width: 1200px; height: 1011px; overflow: hidden; }
  body {
    background: var(--bg);
    font-family: "Raleway", Arial, sans-serif;
    color: var(--ink);
    position: relative;
  }
  .sheet {
    position: absolute;
    background: var(--paper);
    box-shadow: 0 2px 10px rgba(0,0,0,.18);
    overflow: hidden;
  }
  .band { position: absolute; left: 0; bottom: 0; width: 100%; }
  .brand { display: flex; align-items: center; gap: 8px; }
  .brand-mark { background: var(--gold); flex: none; }
  .brand-name { font-weight: 700; color: var(--green); white-space: nowrap; }
  .small { font-size: 9px; line-height: 1.45; color: var(--grey); }
  .web { position: absolute; font-size: 10px; font-weight: 600; color: #fff; letter-spacing: .3px; }

  /* Letterhead */
  .letterhead { left: 60px; top: 120px; width: 580px; height: 750px; }
  .letterhead .brand { position: absolute; left: 40px; top: 40px; }
  .letterhead .brand-mark { width: 30px; height: 30px; }
  .letterhead .brand-name { font-size: 26px; }
  .letterhead .address { position: absolute; right: 40px; top: 40px; text-align: right; }
  .letterhead .web { right: 34px; bottom: 10px; }

  /* Envelope */
  .envelope { left: 690px; top: 120px; width: 450px; height: 195px; }
  .envelope .brand { position: absolute; left: 24px; top: 22px; }
  .envelope .brand-mark { width: 22px; height: 22px; }
  .envelope .brand-name { font-size: 19px; }
  .envelope .return { position: absolute; left: 24px; top: 56px; }
  .envelope .corner { position: absolute; right: 0; top: 0; }
  .envelope .web { right: 22px; bottom: 8px; }

  /* Business card front */
  .card-front { left: 690px; top: 355px; width: 450px; height: 257px; }
  .card-front .brand { position: absolute; left: 28px; top: 26px; }
  .card-front .brand-mark { width: 26px; height: 26px; }
  .card-front .brand-name { font-size: 23px; }
  .card-front .person { position: absolute; left: 28px; top: 86px; }
  .card-front .name { font-size: 13px; font-weight: 700; color: var(--ink); }
  .card-front .title { font-size: 10px; color: var(--grey); margin-bottom: 6px; }
  .card-front .address { position: absolute; left: 28px; top: 170px; }
  .card-front .web { right: 26px; bottom: 9px; }

  /* Card backs */
  .card-back {
    top: 652px; width: 215px; height: 123px;
    color: #fff; text-align: center;
    display: flex; flex-direction: column; align-items: center; justify-content: space-between;
    padding: 12px 10px 10px;
  }
  .card-back.gold { left: 690px; background: linear-gradient(135deg, var(--gold-light), var(--gold) 55%, var(--gold-dark)); }
  .card-back.green { left: 925px; background: linear-gradient(135deg, #708b5f, var(--green) 55%, var(--green-dark)); }
  .card-back .motto { font-size: 9px; letter-spacing: .5px; }
  .card-back .center-mark { width: 40px; height: 40px; }
  .card-back.gold .center-mark { background: var(--gold-dark); }
  .card-back.green .center-mark { background: var(--gold); }
  .card-back .tagline { font-size: 7px; letter-spacing: .2px; }
</style>
</head>
<body>

  <section class="sheet letterhead" aria-label="Letterhead">
    <div class="brand"><span class="brand-mark"></span><span class="brand-name">Harbor Kindle</span></div>
    <p class="address small">2873 Wexbury Ln. Suite 615<br>Naples, FL 34782<br>T: 239 555 0142<br>Lina@HarborKindle.example</p>
    <svg class="band" width="580" height="70" viewBox="0 0 580 70" aria-hidden="true">
      <polygon points="0,34 580,20 580,70 0,70" fill="var(--green)"/>
      <polygon points="330,70 350,40 372,40 352,70" fill="var(--gold)"/>
      <polygon points="356,70 376,40 384,40 364,70" fill="#ffffff" opacity=".7"/>
    </svg>
    <span class="web">www.HarborKindle.example</span>
  </section>

  <section class="sheet envelope" aria-label="Envelope">
    <svg class="corner" width="150" height="80" viewBox="0 0 150 80" aria-hidden="true">
      <polygon points="40,0 150,0 150,80" fill="var(--gold)"/>
    </svg>
    <div class="brand"><span class="brand-mark"></span><span class="brand-name">Harbor Kindle</span></div>
    <p class="return small">2873 Wexbury Ln. Suite 615<br>Naples, FL 34782</p>
    <svg class="band" width="450" height="40" viewBox="0 0 450 40" aria-hidden="true">
      <polygon points="0,18 450,8 450,40 0,40" fill="var(--green)"/>
      <polygon points="200,40 214,18 230,18 216,40" fill="var(--gold)"/>
    </svg>
    <span class="web">www.HarborKindle.example</span>
  </section>

  <section class="sheet card-front" aria-label="Business card front">
    <div class="brand"><span class="brand-mark"></span><span class="brand-name">Harbor Kindle</span></div>
    <div class="person">
      <p class="name">Lina Brook, KLV, DRT</p>
      <p class="title">Executive Life Coach</p>
      <p class="small">T: 239 555 0142<br>Lina@HarborKindle.example</p>
    </div>
    <p class="address small">2873 Wexbury Ln. Suite 615<br>Naples, FL 34782</p>
    <svg class="band" width="450" height="44" viewBox="0 0 450 44" aria-hidden="true">
      <polygon points="0,22 450,12 450,44 0,44" fill="var(--green)"/>
      <polygon points="190,44 205,20 222,20 207,44" fill="var(--gold)"/>
      <polygon points="211,44 226,20 232,20 217,44" fill="#ffffff" opacity=".7"/>
    </svg>
    <span class="web">www.HarborKindle.example</span>
  </section>

  <section class="sheet card-back gold" aria-label="Business card back, gold">
    <p class="motto">rise with purpose</p>
    <span class="center-mark"></span>
    <p class="tagline">Guiding Driven Leaders and Founders Forward.</p>
  </section>

  <section class="sheet card-back green" aria-label="Business card back, green">
    <p class="motto">rise with purpose</p>
    <span class="center-mark"></span>
    <p class="tagline">Guiding Driven Leaders and Founders Forward.</p>
  </section>

</body>
</html>
```